Buisness Card for an Agricultural Contracting and Earthmoving Company

We need a business card for a new business based in Kilmore, Victoria. We are a company that specialises in two areas the first is and Earthmoving company, we do large jobs such as soccer fields to small jobs such as house cuts and riding arena's, drainage, and dams. The other side of the business specialises in Agricultural improvements and hay contracting. We require a card to represent both sides of the business. Must have the following information: Dale Purvick, 2947 Tambrook Rd, Kilmore Victoria 3519, ph:03 5924 3086, mob: 0427 913 648, e-mail: dale@purvickworks.com.au. Earthmoving and Agricultural Contracting.

Target Market(s)

Builder's, Council's, new home buyers, Farmers

Industry/Entity Type

House

Font styles to use
Sans Serif

Colors
ec2026
000000
5c5c5c
ffffff

Requirements
Must have
• Both facets of the business represented. Company logo

```html
<!DOCTYPE html>
<html lang="en">
<head>
<meta charset="utf-8">
<title>Purvick Works – Business Card</title>
<link rel="stylesheet" href="https://fonts.googleapis.com/css2?family=Saira+Semi+Condensed:wght@700&family=Arimo:wght@400;700&display=swap">
<style>
  :root {
    --brand-red: #ec2026;
    --brand-red-deep: #8e1a22;
    --ink: #000000;
    --ink-soft: #5c5c5c;
    --paper: #ffffff;
    --backdrop: #8a8a8a;
  }
  * { box-sizing: border-box; margin: 0; padding: 0; }
  html, body {
    width: 1200px; height: 901px; overflow: hidden;
    background: var(--backdrop);
    font-family: "Arimo", Arial, sans-serif;
  }
  .sheet {
    position: relative; width: 1200px; height: 901px;
    display: flex; align-items: center; justify-content: center; gap: 40px;
  }
  .card {
    position: relative; width: 540px; height: 330px;
    background: var(--paper); overflow: hidden;
  }
  .card__band {
    position: absolute; right: 0; bottom: 0; height: 24px;
    background: linear-gradient(90deg, var(--brand-red-deep), var(--brand-red) 55%);
  }
  .card--front .card__band { left: 50%; }
  .card--back .card__band { left: 56%; }
  .brand { position: absolute; display: flex; align-items: center; gap: 18px; }
  .card--front .brand { left: 44px; top: 92px; }
  .card--back .brand { left: 60px; top: 128px; }
  .brand__square { width: 56px; height: 56px; background: var(--brand-red); flex: none; }
  .brand__name {
    font-family: "Saira Semi Condensed", "Arial Narrow", sans-serif;
    font-weight: 700; font-size: 30px; line-height: 1; letter-spacing: 0.5px;
    color: var(--brand-red); text-transform: uppercase; white-space: nowrap;
  }
  .brand__tagline {
    margin-top: 4px; font-size: 14px; color: var(--ink); white-space: nowrap;
  }
  .contact {
    position: absolute; left: 118px; top: 170px;
    font-size: 11.5px; line-height: 1.38; color: var(--ink-soft);
    font-style: normal; white-space: nowrap;
  }
  .contact__name { font-weight: 700; color: var(--ink); font-size: 12px; margin-bottom: 2px; }
</style>
</head>
<body>
<main class="sheet">
  <section class="card card--front" aria-label="Business card front">
    <div class="brand">
      <span class="brand__square" aria-hidden="true"></span>
      <div>
        <div class="brand__name">Purvick Works</div>
        <div class="brand__tagline">Earthmoving and Agricultural Contracting.</div>
      </div>
    </div>
    <address class="contact">
      <div class="contact__name">Dale Purvick</div>
      <div>2947 Tambrook Rd,</div>
      <div>Wattlebrook Vale 3519</div>
      <div>ph:03 5924 3086</div>
      <div>mob: 0427 913 648</div>
      <div>dale@purvickworks.com.au.</div>
    </address>
    <div class="card__band"></div>
  </section>

  <section class="card card--back" aria-label="Business card back">
    <div class="brand">
      <span class="brand__square" aria-hidden="true"></span>
      <div>
        <div class="brand__name">Purvick Works</div>
        <div class="brand__tagline">Earthmoving and Agricultural Contracting.</div>
      </div>
    </div>
    <div class="card__band"></div>
  </section>
</main>
</body>
</html>
```